Speisekarten für ein Seerestaurant/Pizzeria
Zielgruppe
Wir sin ein Seerestaurant/Pizzeria in einem Ferien Ort
Aufgabenstellung
Wir brauchen Speisekarte in A4 und A5 Format und wichtig dass wir das Inhalt immer einfach bearbeiten können

```html
<!DOCTYPE html>
<html lang="de">
<head>
<meta charset="utf-8">
<title>Uferli – Speisekarte</title>
<link href="https://fonts.googleapis.com/css2?family=Abel&family=Oswald:wght@400;500;600&family=Open+Sans:ital,wght@0,700;1,400;1,600&family=Allura&display=swap" rel="stylesheet">
<style>
:root{
  --stage:#d9dadc;
  --navy:#0b3a50;
  --navy-soft:#134a63;
  --cream:#f6f8ef;
  --ink:#2b3b45;
  --red:#9b1c24;
  --gold:#e9dfb4;
  --script:#4d7aa3;
}
*{margin:0;padding:0;box-sizing:border-box}
html,body{width:1200px;height:2296px;overflow:hidden}
body{background:var(--stage);position:relative;font-family:"Abel",sans-serif;color:var(--ink)}
.page{position:absolute;width:560px;height:792px;background:var(--cream);box-shadow:0 4px 14px rgba(0,0,0,.12)}
.abs{position:absolute}

/* cover */
.cover{left:320px;top:260px}
.pattern-band{position:absolute;top:0;width:141px;height:100%;background:linear-gradient(180deg,var(--navy) 0%,var(--navy-soft) 50%,var(--navy) 100%)}
.pattern-band.left{left:0}.pattern-band.right{right:0}
.cover-panel{position:absolute;left:141px;width:278px;top:0;height:100%;text-align:center}
.brand-name{position:absolute;left:0;right:0;top:312px;font-family:"Oswald",sans-serif;font-weight:600;font-size:62px;line-height:1;color:#222}
.brand-mark{width:14px;height:14px;background:#222;border-radius:50%;margin:0 auto 14px;position:absolute;left:132px;top:284px}
.tagline{position:absolute;left:0;right:0;top:478px;font-size:20px;letter-spacing:4px;line-height:31px;color:#222}
.delivery{position:absolute;left:22px;right:22px;top:650px;height:57px;border:1px solid #8a949a;font-family:"Open Sans",sans-serif;font-weight:700;font-size:10.5px;letter-spacing:1.6px;line-height:16px;color:var(--navy);padding-top:12px}
.address{position:absolute;left:0;right:0;top:742px;font-size:11px;letter-spacing:1px;line-height:18px;color:#222}

/* spread */
.spread-left{left:40px;top:1180px}
.spread-right{left:600px;top:1180px}
.soup-col{position:absolute;left:0;top:0;width:266px;height:100%}
.host-photo{position:absolute;left:29px;top:36px;width:213px;height:269px;background:linear-gradient(180deg,#3f7fbf 0%,#2b4f78 45%,#1e2f47 100%)}
.host-caption{position:absolute;left:120px;top:248px;width:92px;text-align:center;font-family:"Open Sans",sans-serif;font-size:7px;color:#fff}
.host-caption b{display:block;border-bottom:1px solid rgba(255,255,255,.6);padding-bottom:2px;margin-bottom:2px}
.greeting{position:absolute;left:28px;top:324px;width:215px;font-family:"Allura",cursive;font-size:30px;line-height:28px;color:var(--script);transform:rotate(-5deg)}
.greeting span{display:block;padding-left:24px}
.team{position:absolute;right:26px;top:384px;font-size:8px;color:#445}
.section-title{font-family:"Oswald",sans-serif;font-weight:500;letter-spacing:6px;text-align:center}
.suppen-title{position:absolute;left:0;width:266px;top:430px;font-size:25px;color:var(--navy)}
.item{position:absolute;font-size:13px;letter-spacing:.6px;text-transform:none}
.item .name{display:block}
.desc{display:block;font-family:"Open Sans",sans-serif;font-style:italic;font-size:8.4px;line-height:11.5px;margin-top:6px;letter-spacing:0}
.price{position:absolute;font-family:"Open Sans",sans-serif;font-weight:700;font-size:7.5px;text-align:right;line-height:11px}
.price small{display:block;font-weight:400;font-size:6px}
.soup .item{left:46px;color:#333}
.soup .desc{color:var(--navy);margin-top:3px}
.soup .price{right:324px;color:var(--navy)}

.salad-col{position:absolute;left:293px;top:0;width:267px;height:100%;background:var(--navy);color:#e8ecdf}
.salad-col .section-title{position:absolute;left:0;right:0;top:58px;font-size:25px;color:var(--gold)}
.rule{position:absolute;left:100px;width:67px;top:105px;border-top:1px solid var(--gold)}
.salad-intro{position:absolute;left:40px;right:40px;top:122px;text-align:center;font-family:"Open Sans",sans-serif;font-style:italic;font-weight:600;font-size:8.4px;line-height:12px;color:#fff}
.salad-col .item{left:38px;width:150px;color:var(--gold)}
.salad-col .desc{color:#c9d2cf}
.salad-col .price{right:30px;color:#fff}

.main-box{position:absolute;left:27px;top:28px;width:510px;height:349px;background:var(--navy);color:#e8ecdf}
.main-box .section-title{position:absolute;left:0;right:0;top:30px;font-size:25px;color:#fff;letter-spacing:7px}
.main-box .item{width:170px;color:#fff}
.main-box .desc{color:#c9d2cf}
.main-box .price{color:#fff}

.bbq{position:absolute;left:27px;top:401px;width:510px;height:366px;border-left:1.5px solid var(--red);border-right:1.5px solid var(--red);color:var(--red)}
.bbq .section-title{position:absolute;left:0;right:0;top:26px;font-size:25px;letter-spacing:6px}
.bbq-sub{position:absolute;left:0;right:0;top:60px;text-align:center;font-family:"Oswald",sans-serif;font-size:17px;letter-spacing:1.5px}
.bbq-intro{position:absolute;left:70px;right:70px;top:122px;text-align:center;font-family:"Open Sans",sans-serif;font-style:italic;font-weight:600;font-size:8.4px;line-height:12px}
.bbq .item{width:170px}
.bbq .desc{color:var(--red)}
</style>
</head>
<body>

<!-- Cover -->
<section class="page cover">
  <div class="pattern-band left" role="img" aria-label="Blaues Muster mit gezeichneten Speisen und Getränken"></div>
  <div class="cover-panel">
    <div class="brand-mark"></div>
    <div class="brand-name">Uferli</div>
    <div class="tagline">Seerestaurant<br>RIEDHALDE – Seewil</div>
    <div class="delivery">PIZZA LIEFERUNG<br>041 555 01 23</div>
    <div class="address">Uferweg 12 • 6399 Seewil<br>uferli-see.ch</div>
  </div>
  <div class="pattern-band right" role="img" aria-label="Blaues Muster mit gezeichneten Speisen und Zutaten"></div>
</section>

<!-- Spread left page -->
<section class="page spread-left">
  <div class="soup-col soup">
    <div class="host-photo" role="img" aria-label="Foto des Gastgebers mit Pizzaschaufel vor dem See"></div>
    <div class="host-caption"><b>Marco Brenner</b>Gastgeber</div>
    <div class="greeting">En Guete<span>wünscht Ihnen</span></div>
    <div class="team">Ihr Seerestaurant RIEDHALDE-Team</div>
    <h2 class="section-title suppen-title">SUPPEN</h2>

    <div class="item" style="top:494px"><span class="name">BOUILLON</span><span class="desc">mit Tortelloni</span></div>
    <div class="price" style="top:496px">CHF 10.50</div>

    <div class="item" style="top:538px"><span class="name">GULASCHSUPPE</span><span class="desc">...die Echte – nach ungarischer Art</span></div>
    <div class="price" style="top:538px"><small>kl. Portion</small>CHF 13.50<small>kl. Portion</small>CHF 20.50</div>

    <div class="item" style="top:608px"><span class="name">MINESTRONE</span></div>
    <div class="price" style="top:610px">CHF 11.50</div>

    <div class="item" style="top:640px"><span class="name">TAGESSUPPE</span><span class="desc">fragen Sie unser Personal</span></div>
    <div class="price" style="top:642px">CHF 11.50</div>
  </div>

  <div class="salad-col">
    <h2 class="section-title">SALATE</h2>
    <div class="rule"></div>
    <p class="salad-intro">Alle Salate sind mit hausgemachter Salatsauce Ihrer Wahl und frischem Pizzabrot</p>

    <div class="item" style="top:212px"><span class="name">BURRATA</span><span class="desc">Italienischer Frischkäse, mit frischem Basilikum, extra natives Olivenöl, Balsamico Crema und Cherry Tomaten</span></div>
    <div class="price" style="top:214px">CHF 10.50</div>

    <div class="item" style="top:291px"><span class="name">CEASAR SALAT</span><span class="desc">mit Speck, Croûtons und Parmigiano DOP</span></div>
    <div class="price" style="top:293px">CHF 10.50</div>

    <div class="item" style="top:352px"><span class="name">GEMISCHTER SALAT</span></div>
    <div class="price" style="top:354px">CHF 10.50</div>

    <div class="item" style="top:388px"><span class="name">GRÜNER SALAT</span></div>
    <div class="price" style="top:390px">CHF 10.50</div>

    <div class="item" style="top:425px"><span class="name">NÜSSLISALAT</span><span class="desc">mit Speck, Brotcroûtons und Ei</span></div>
    <div class="price" style="top:427px">CHF 10.50</div>

    <div class="item" style="top:484px"><span class="name">SALAT «RIEDHALDE»</span><span class="desc">Eisberg Salat, Speck, Croutons, Parmigiano DOP und Pouletstreifen</span></div>
    <div class="price" style="top:486px">CHF 10.50</div>
  </div>
</section>

<!-- Spread right page -->
<section class="page spread-right">
  <div class="main-box">
    <h2 class="section-title">HAUPTGERICHTE</h2>

    <div class="item" style="left:33px;top:98px"><span class="name">BEEFSTEAK TARTAR</span><span class="desc">aus Schweizer-Qualitätsrindfleisch abgeschmeckt nach Ihrem Wunsch, serviert mit Toastbrot und Butter</span></div>
    <div class="price" style="left:186px;top:100px">CHF 10.50</div>

    <div class="item" style="left:33px;top:179px"><span class="name">CHICKEN-FINGERS</span><span class="desc">hausgemachte, panierte Pouletstreifen, dazu sweet Chili-Sauce und Pommes Frites</span></div>
    <div class="price" style="left:186px;top:179px">CHF 10.50</div>

    <div class="item" style="left:33px;top:249px"><span class="name">CORDON BLEU</span><span class="desc">«das Klassische» vom Schwein, gefüllt mit Vorderschinken, Raclette und würzigem Gruyère serviert mit Pommes Frites und Gemüse</span></div>
    <div class="price" style="left:186px;top:251px">CHF 10.50</div>

    <div class="item" style="left:289px;top:98px"><span class="name">GYROS-TELLER</span><span class="desc">mit Schweinefleisch serviert mit Salat-Bouquet, Tzatziki-Sauce und Pommes Frites</span></div>
    <div class="price" style="left:440px;top:100px">CHF 10.50</div>

    <div class="item" style="left:289px;top:181px"><span class="name">WIENER SCHNITZEL</span><span class="desc">vom Kalb mit Pommes Frites und Preiselbeeren</span></div>
    <div class="price" style="left:440px;top:179px">CHF 10.50</div>
  </div>

  <div class="bbq">
    <h2 class="section-title">BARBECUE SPEZIALITÄTEN</h2>
    <div class="bbq-sub">AUS DEM SMOKER</div>
    <p class="bbq-intro">Barbecue Gerichte werden 6-12 Stunden im Smoker gegart. Wir verwenden ausschliesslich Schweizer Fleisch und Bio Hickory Holz für das typische BBQ-Erlebnis und Rauch-Aroma.</p>

    <div class="item" style="left:33px;top:186px"><span class="name">BBQ SPARE RIBS</span><span class="desc">aus dem Smoker mit Cherry-Bomb Glasur serviert mit Pommes Frites</span></div>
    <div class="price" style="left:186px;top:188px">CHF 10.50</div>

    <div class="item" style="left:33px;top:255px"><span class="name">PULLED BEEF Burger</span><span class="desc">Hausgemachte Bun, Pulled Beef (180g), BBQ-Sauce, Cheddar-Käse, Coleslaw (Kabissalat) und Jalapeno, serviert mit Pommes</span></div>
    <div class="price" style="left:186px;top:257px">CHF 10.50</div>

    <div class="item" style="left:289px;top:186px"><span class="name">PULLED PORK Burger</span><span class="desc">Hausgemachte Bun, Pulled Pork (180g), BBQ-Sauce, Cheddar-Käse, Coleslaw (Kabissalat) und Jalapeno, serviert mit Pommes</span></div>
    <div class="price" style="left:440px;top:188px">CHF 10.50</div>

    <div class="item" style="left:289px;top:280px"><span class="name">PULLED VEGI Burger</span><span class="desc">Hausgemachte Bun, BBQ-Sauce, Cheddar-Käse, Coleslaw (Kabissalat) und Jalapeno, serviert mit Pommes</span></div>
    <div class="price" style="left:440px;top:282px">CHF 10.50</div>
  </div>
</section>

</body>
</html>
```